Brackenfold Latches Business Cards

Need high quality business card designed around my company logo. Ideally the cards need to be a glossy black as the logo goes well with a black background.

The company is a Locksmithing business.

Domestic clients are Residential Home Owners and Landlords. Commercial clients are local businesses, estate agents, landlords, solicitors

Services offered :
Emergency Lock Out
New Lock Fitting & Replacement
High Security Upgrades
UPVC lock repairs
Mobile Key Cutting
Free Security Reviews

Qualificatons & Certifications:
Accredited Guild & Tower KSR Level 3, QTRB
Fully Insured
PVX Checked

Contact & Business Details:

Business Name : Brackenfold Latches
Name: Rob Fenwick
Tel: 01823 574419 Office / 07841592637 Mobile
Email: contact@brackenfoldlatches.com
Website: www.brackenfoldlatches.com

(please note that the website is currently under development and not available to view)

Locksmith

Name: Rob Fenwick

Services:
Emergency Lock Out
High Security Upgrades
UPVC lock repairs
Mobile Key Cutting
Free Security Reviews

• Ideally the cards should be a glossy black as the logo stands out better on a black background.

Logo on front and the word LOCKSMITH should be incorporated into the front design of the card.

Qualifications & Certifications on the back ideally along the top / bottom of the card or split (I.e along the top “ Accredited : Guild & Tower Level 3 , QTRB”
and along the bottom , “Fully Insured & PVX Checked”

Services offered ideally listed on the back of the card, preferably split into two columns. If possible the logo could also be incorporated onto the back of the card between the two services columns (I.e the services listed either side of the logo)
• On the back of the card, have the logo in the middle with the services listed either side of the logo I.e 3 services on left of logo and three to the right.

```html
<!DOCTYPE html>
<html lang="en">
<head>
<meta charset="utf-8">
<title>Brackenfold Latches Business Cards</title>
<link href="https://fonts.googleapis.com/css2?family=Cinzel:wght@500;600&family=Arimo:wght@400&display=swap" rel="stylesheet">
<style>
  :root {
    --backdrop: #4a4a4a;
    --card: #070707;
    --gold: #d9a92a;
    --gold-edge: #b8892a;
    --ink-light: #f2f2f2;
    --accent-dot: #f08c1a;
    --divider: #5a5a5a;
  }
  * { box-sizing: border-box; margin: 0; padding: 0; }
  html, body {
    width: 1200px; height: 800px; overflow: hidden;
    background: var(--backdrop);
  }
  .sheet {
    width: 1200px; height: 800px;
    display: flex; align-items: center; justify-content: center; gap: 40px;
  }
  .card {
    position: relative;
    width: 560px; height: 320px;
    background: var(--card);
    border: 1px solid var(--gold-edge);
    box-shadow: 0 14px 30px rgba(0,0,0,0.45);
    overflow: hidden;
  }

  /* Front */
  .front-brand {
    position: absolute; left: 0; top: 0; width: 260px; height: 100%;
    display: flex; align-items: center; justify-content: center; gap: 10px;
  }
  .brand-dot {
    width: 14px; height: 14px; border-radius: 50%; background: var(--gold);
    flex: none;
  }
  .brand-name {
    font-family: "Cinzel", serif; font-weight: 600; color: var(--gold);
    font-size: 19px; letter-spacing: 1px; line-height: 1.2;
  }
  .front-divider {
    position: absolute; left: 262px; top: 40px; width: 1px; height: 240px;
    background: linear-gradient(to bottom, transparent, var(--divider), transparent);
  }
  .contact-block {
    position: absolute; left: 292px; top: 62px;
  }
  .company {
    font-family: "Cinzel", serif; font-weight: 600; color: var(--gold);
    font-size: 18px; letter-spacing: 1px;
  }
  .person {
    font-family: "Arimo", sans-serif; color: var(--ink-light);
    font-size: 14px; margin-top: 4px;
  }
  .contact-list { list-style: none; margin-top: 26px; }
  .contact-list li {
    display: flex; align-items: center; gap: 9px;
    font-family: "Arimo", sans-serif; color: var(--ink-light);
    font-size: 12.5px; line-height: 1.55;
  }
  .contact-list svg { width: 12px; height: 12px; flex: none; fill: var(--gold); }
  .role {
    position: absolute; right: 34px; bottom: 34px;
    font-family: "Cinzel", serif; font-weight: 600; color: var(--gold);
    font-size: 16px; letter-spacing: 2px;
  }

  /* Back */
  .back { display: flex; flex-direction: column; align-items: center; }
  .accreditation {
    margin-top: 30px;
    font-family: "Cinzel", serif; font-weight: 500; color: var(--gold);
    font-size: 13px; letter-spacing: 0.5px;
  }
  .back-brand {
    margin-top: 48px;
    display: flex; align-items: center; gap: 10px;
  }
  .back-brand .brand-name { font-size: 24px; }
  .services {
    margin-top: 44px; text-align: center;
    font-family: "Arimo", sans-serif; color: var(--ink-light);
    font-size: 13.5px; line-height: 1.45;
  }
  .services .key {
    display: inline-block; width: 7px; height: 11px; margin: 0 6px -1px;
    vertical-align: baseline;
  }
  .services .key svg { width: 7px; height: 11px; fill: var(--gold); display: block; }
  .assurances {
    margin-top: 18px;
    font-family: "Cinzel", serif; font-weight: 600; color: var(--gold);
    font-size: 13px; letter-spacing: 0.5px;
  }
  .assurances .sep { color: var(--accent-dot); margin: 0 5px; }
</style>
</head>
<body>
<main class="sheet">

  <section class="card front" aria-label="Business card front">
    <div class="front-brand">
      <span class="brand-dot"></span>
      <span class="brand-name">Brackenfold Latches</span>
    </div>
    <div class="front-divider"></div>
    <div class="contact-block">
      <p class="company">Brackenfold Latches</p>
      <p class="person">Rob Fenwick</p>
      <ul class="contact-list">
        <li>
          <svg viewBox="0 0 24 24"><path d="M6.6 10.8a15.1 15.1 0 0 0 6.6 6.6l2.2-2.2a1 1 0 0 1 1-.25 11.4 11.4 0 0 0 3.6.57 1 1 0 0 1 1 1V20a1 1 0 0 1-1 1A17 17 0 0 1 3 4a1 1 0 0 1 1-1h3.5a1 1 0 0 1 1 1c0 1.25.2 2.45.57 3.57a1 1 0 0 1-.25 1z"/></svg>
          01823 574419
        </li>
        <li>
          <svg viewBox="0 0 24 24"><path d="M7 1h10a2 2 0 0 1 2 2v18a2 2 0 0 1-2 2H7a2 2 0 0 1-2-2V3a2 2 0 0 1 2-2zm0 3v14h10V4zm5 15.5a1.2 1.2 0 1 0 0 2.4 1.2 1.2 0 0 0 0-2.4z"/></svg>
          07841592637
        </li>
        <li>
          <svg viewBox="0 0 24 24"><path d="M2 5h20v14H2zm2 2v.5l8 5 8-5V7zm0 2.9V17h16V9.9l-8 5z"/></svg>
          contact@brackenfoldlatches.com
        </li>
        <li>
          <svg viewBox="0 0 24 24"><path d="M12 2a10 10 0 1 0 0 20 10 10 0 0 0 0-20zm6.9 6h-2.8a15 15 0 0 0-1.3-3.6A8 8 0 0 1 18.9 8zM12 4c.8 1.2 1.5 2.5 1.9 4h-3.8c.4-1.5 1.1-2.8 1.9-4zM4.3 14a8 8 0 0 1 0-4h3.3a16 16 0 0 0 0 4zm.8 2h2.8c.3 1.3.8 2.5 1.3 3.6A8 8 0 0 1 5.1 16zm2.8-8H5.1a8 8 0 0 1 4.1-3.6C8.7 5.5 8.2 6.7 7.9 8zM12 20c-.8-1.2-1.5-2.5-1.9-4h3.8c-.4 1.5-1.1 2.8-1.9 4zm2.3-6H9.7a14 14 0 0 1 0-4h4.6a14 14 0 0 1 0 4zm.5 5.6c.5-1.1 1-2.3 1.3-3.6h2.8a8 8 0 0 1-4.1 3.6zm1.6-5.6a16 16 0 0 0 0-4h3.3a8 8 0 0 1 0 4z"/></svg>
          www.brackenfoldlatches.com
        </li>
      </ul>
    </div>
    <p class="role">Locksmith</p>
  </section>

  <section class="card back" aria-label="Business card back">
    <p class="accreditation">Accredited Guild &amp; Tower KSR Level 3, QTRB</p>
    <div class="back-brand">
      <span class="brand-dot"></span>
      <span class="brand-name">Brackenfold Latches</span>
    </div>
    <div class="services">
      <p><span class="key"><svg viewBox="0 0 7 11"><circle cx="3.5" cy="2.5" r="2.5"/><rect x="2.6" y="4" width="1.8" height="7"/><rect x="4.4" y="8" width="1.8" height="1.3"/></svg></span>Emergency Lock Out<span class="key"><svg viewBox="0 0 7 11"><circle cx="3.5" cy="2.5" r="2.5"/><rect x="2.6" y="4" width="1.8" height="7"/><rect x="4.4" y="8" width="1.8" height="1.3"/></svg></span>New Lock Fitting &amp; Replacement</p>
      <p>High Security Upgrades<span class="key"><svg viewBox="0 0 7 11"><circle cx="3.5" cy="2.5" r="2.5"/><rect x="2.6" y="4" width="1.8" height="7"/><rect x="4.4" y="8" width="1.8" height="1.3"/></svg></span>UPVC lock repairs<span class="key"><svg viewBox="0 0 7 11"><circle cx="3.5" cy="2.5" r="2.5"/><rect x="2.6" y="4" width="1.8" height="7"/><rect x="4.4" y="8" width="1.8" height="1.3"/></svg></span>Mobile Key Cutting</p>
      <p>Free Security Reviews</p>
    </div>
    <p class="assurances">Fully Insured<span class="sep">&#8226;</span>PVX Checked</p>
  </section>

</main>
</body>
</html>
```